QUOTE Graphics for Summer Challenge

I would like to put these quotes over one of the pictures attached; For Instagram, use new size: 4:5 (1080 x 1350 pixels). One Quote per picture, and I want the quote to be bold or easy to read as well. I provided a few reference graphics that I really like as examples below.
All of the pictures are attached; you can pick any photo and add one quote to it; but no stock photography
All the quotes are in the attached WORD document

```html
<!DOCTYPE html>
<html lang="en">
<head>
<meta charset="utf-8">
<title>Sunlit Summer Reset – Quote Graphics</title>
<link href="https://fonts.googleapis.com/css2?family=Bebas+Neue&display=swap" rel="stylesheet">
<style>
  :root {
    --board: #1b3752;
    --sky: #8fc3e6;
    --pool: #4fa7d6;
    --hills: #8a7a64;
    --skin: #7a4a32;
    --deck: #d9cfc6;
    --band: rgba(104, 84, 122, 0.78);
    --quote: #ffffff;
  }
  * { margin: 0; padding: 0; box-sizing: border-box; }
  html, body { width: 1200px; height: 600px; overflow: hidden; background: var(--board); }
  .board {
    width: 1200px; height: 600px;
    display: grid;
    grid-template-columns: repeat(5, 224px);
    grid-template-rows: repeat(2, 280px);
    column-gap: 9.5px; row-gap: 9px;
    padding: 13px 19px;
  }
  .post { position: relative; overflow: hidden; }
  .post__photo { position: absolute; inset: 0; }
  .photo--deck { background: linear-gradient(180deg, var(--sky) 0%, var(--hills) 30%, var(--pool) 55%, var(--deck) 75%, var(--skin) 100%); }
  .photo--pool { background: linear-gradient(180deg, var(--sky) 0%, var(--pool) 50%, var(--skin) 72%, #9fd3ee 100%); }
  .photo--hills { background: linear-gradient(180deg, #b7d2e4 0%, #6f7e5c 35%, var(--skin) 70%, #4e5a3c 100%); }
  .post__band {
    position: absolute; top: 0; bottom: 0; width: 112px;
    background: var(--band);
    display: flex; align-items: center; justify-content: center;
  }
  .band--l0 { left: 0; }
  .band--l3 { left: 3px; }
  .band--l4 { left: 4px; }
  .band--l9 { left: 9px; }
  .band--l10 { left: 10px; }
  .band--r1 { left: 105px; }
  .band--r2 { left: 101px; }
  .quote {
    font-family: "Bebas Neue", "Oswald", sans-serif;
    color: var(--quote);
    font-size: 17px; line-height: 20.6px;
    text-align: center; letter-spacing: -0.4px;
    white-space: nowrap;
  }
</style>
</head>
<body>
<main class="board">
  <article class="post">
    <div class="post__photo photo--deck" role="img" aria-label="Woman in a sheer brown gown posing by an infinity pool"></div>
    <div class="post__band band--l10"><p class="quote">Feeling bloated,<br>sluggish,<br>and too big?<br>Your detox starts<br>now.<br>Comment summer<br>to join the<br>sunlit summer<br>reset</p></div>
  </article>
  <article class="post">
    <div class="post__photo photo--pool" role="img" aria-label="Woman in a leopard bikini sitting at the pool edge"></div>
    <div class="post__band band--l4"><p class="quote">You don't need<br>motivation.<br>You need<br>a proven plan and<br>some accountability.<br>Comment<br>sunlit to get<br>join us July 7th</p></div>
  </article>
  <article class="post">
    <div class="post__photo photo--pool" role="img" aria-label="Woman in a black bikini standing in an infinity pool"></div>
    <div class="post__band band--l3"><p class="quote">We're getting<br>a tiny waist and<br>dropping<br>pounds<br>together.<br>Don't miss this.<br>Comment<br>sunlit to join</p></div>
  </article>
  <article class="post">
    <div class="post__photo photo--deck" role="img" aria-label="Woman in a sheer brown gown on a pool deck"></div>
    <div class="post__band band--l10"><p class="quote">The scale keeps<br>climbing and<br>nothing's working?<br>This challenge is<br>your lifeline.<br>Comment sunlit<br>to join now!</p></div>
  </article>
  <article class="post">
    <div class="post__photo photo--hills" role="img" aria-label="Woman in a brown crochet outfit with hills behind"></div>
    <div class="post__band band--l4"><p class="quote">This sunlit<br>summer<br>reset plan is<br>helping women<br>drop pounds and<br>feel sexy again.<br>Comment<br>summer to join us</p></div>
  </article>

  <article class="post">
    <div class="post__photo photo--hills" role="img" aria-label="Woman in a brown crochet outfit on a lawn"></div>
    <div class="post__band band--l0"><p class="quote">Summer's here,<br>but your body<br>doesn't feel ready?<br>You're not too late.<br>Comment<br>summer to join<br>the sunlit<br>summer reset</p></div>
  </article>
  <article class="post">
    <div class="post__photo photo--hills" role="img" aria-label="Woman in a sheer brown gown by a pool with hills behind"></div>
    <div class="post__band band--r1"><p class="quote">Your belly bloat and<br>stubborn weight<br>gain aren't<br>going anywhere…<br>unless you do<br>something different.<br>Comment<br>sunlit to join us!</p></div>
  </article>
  <article class="post">
    <div class="post__photo photo--pool" role="img" aria-label="Woman in sunglasses and black swimsuit at the pool edge"></div>
    <div class="post__band band--r2"><p class="quote">Cravings,<br>belly fat,<br>and water weight?<br>Say goodbye in<br>30 days. Comment<br>summer to<br>join the sunlit<br>summer<br>reset</p></div>
  </article>
  <article class="post">
    <div class="post__photo photo--pool" role="img" aria-label="Woman in a leopard bikini seated by the pool"></div>
    <div class="post__band band--l9"><p class="quote">Need a jumpstart?<br>We're detoxing,<br>burning fat,<br>and getting<br>snatched.<br>Comment sunlit<br>to join us on<br>July 7th</p></div>
  </article>
  <article class="post">
    <div class="post__photo photo--pool" role="img" aria-label="Woman in sunglasses climbing out of an infinity pool"></div>
    <div class="post__band band--l4"><p class="quote">If you feel like<br>you've let<br>yourself go lately,<br>this is your<br>jumpstart.<br>Comment summer to<br>join the sunlit<br>summer reset</p></div>
  </article>
</main>
</body>
</html>
```